App for Lawyers & Accountants needs 'Professional' Styling

We want to style our app to convey a 'Professional' appearance. It's used by Lawyers, Accountants, Doctors etc. who take their work very seriously.

We currently trying to follow corvane layout guidelines, but we find our app looks very bland. I've uploaded a screenshot of our current app, and two mock-ups of more stylized versions, but we're not happy with those mock-ups.

We'd like to see alternate designs for those two mock-ups, that look much more professional.

The specific elements we'd like to improve/focus on are:
* Colour of the top and left nav bars
* Appearance of the left nav, size, icons spacing
* Appearance of the buttons on the top right, so the user knows they are buttons they can press
* Spacing of the dashboard, background colour and spacing, colour/layout of the 'overdue' and 'todo' accordion headings in the 'my tasks' section.
* List view background grey, to be consistent with dashboard, but unobtrusive
* List view tabs to be obvious as tabs, but 'saved searches', filters and the export icon to still be associated with the data displayed, but it should be obvious to the user that those are different buttons, not just more tabs. (I.e. the filters button opens a panel below it that allows the user to filter the data in the list.)
* General appearance of the popup menu when you push the 'add' button on the top right

However, despite those specifics I'm sure it's all the subtle elements of the design that make a big difference.

Our brand colour is 1D4F91, and we use A20067 as a secondary colour in print media, (although it doesn't seem to work to well within the app.) Our brand font is signika. We'd like the designs to be based on those colours & font.

Professional people, Lawyers, Accountants, Doctors etc.

Sans Serif
• Signika

0255a3

• The most 'Professional' experience/quality possible. Think the quality & brand image of brindlewave desk, but taken to a higher level.
• An example/mock-up of the dashboard, list view and 'add' item popup menu
• Display the dashboard cards with the same information as our mock-ups - the information there is important and we don't have any extra cards to add (in the near term)
• Various colour combinations for the top and left nav bars, based on our primary blue brand colour, and perhaps some shade of dark grey.

```html
<!DOCTYPE html>
<html lang="en">
<head>
<meta charset="utf-8">
<title>Matters</title>
<link href="https://fonts.googleapis.com/css2?family=Signika:wght@300;400;600&display=swap" rel="stylesheet">
<style>
:root{
  --brand:#1d4f91;
  --brand-dark:#1b3f78;
  --page:#f2f4f7;
  --band:#f4f6f9;
  --line:#e3e6eb;
  --ink:#2e3440;
  --muted:#5d6470;
  --soft:#9aa1ab;
  --white:#ffffff;
}
*{box-sizing:border-box;margin:0;padding:0}
html,body{width:1200px;height:775px;overflow:hidden}
body{font-family:"Signika",sans-serif;background:var(--page);color:var(--ink);position:relative}
.abs{position:absolute}
.sidebar{left:0;top:0;width:61px;height:775px;background:var(--brand)}
.side-icon{position:absolute;left:18px;width:24px;height:24px}
.side-active{position:absolute;left:0;top:136px;width:4px;height:22px;background:var(--white)}
.topbar{left:61px;top:0;width:1139px;height:60px;background:var(--white);box-shadow:0 1px 3px rgba(0,0,0,.05)}
.search-label{left:130px;top:22px;font-size:13px;color:var(--muted)}
.add-btn{left:800px;top:15px;width:97px;height:29px;border-radius:15px;background:var(--brand-dark);color:var(--white);font-size:13px;font-weight:600;display:flex;align-items:center;padding-left:9px;gap:8px}
.add-btn .plus{width:17px;height:17px;border-radius:50%;background:var(--brand);display:flex;align-items:center;justify-content:center}
.avatar{left:1035px;top:15px;width:30px;height:30px;border-radius:50%;background:linear-gradient(135deg,#b9a99a,#6d6a69)}
.user-name{left:1077px;top:22px;font-size:12.5px;color:var(--ink)}
.card{left:99px;top:99px;width:1062px;height:575px;background:var(--white);border-radius:2px}
.toolbar{left:99px;top:99px;width:1062px;height:53px;background:var(--band)}
.tab{top:118px;font-size:11px;color:var(--muted)}
.tab.active{color:var(--brand);font-weight:600;font-size:12px}
.tab-underline{left:135px;top:148px;width:61px;height:2px;background:var(--brand)}
.ctl{border:1px solid var(--brand);border-radius:2px;background:var(--white);color:var(--brand);font-size:11px;font-weight:600;display:flex;align-items:center;padding-left:13px}
.export{left:1064px;top:110px;width:84px;height:30px;background:var(--brand);border-radius:2px;color:var(--white);font-size:12.5px;font-weight:600;display:flex;align-items:center;justify-content:center;gap:6px}
.th{top:171px;font-size:12px;font-weight:600;color:var(--ink)}
.row-line{left:135px;width:981px;height:1px;background:var(--line)}
.td{font-size:12px;color:var(--muted);letter-spacing:.3px}
.menu{left:703px;top:51px;width:198px;height:270px;background:var(--white);box-shadow:0 2px 8px rgba(0,0,0,.18);border-radius:2px}
.menu-caret{left:872px;top:45px;width:12px;height:12px;background:var(--white);transform:rotate(45deg)}
.menu-head{height:38px;padding:13px 0 0 14px;font-size:12px;color:var(--brand);border-bottom:1px solid var(--line)}
.menu-item{height:38px;display:flex;align-items:center;gap:14px;padding-left:20px;font-size:12px;font-weight:600;color:var(--ink);border-bottom:1px solid var(--line)}
.menu-item:last-child{border-bottom:0}
.menu-item.hover{background:#f1f3f6}
.menu-item svg{width:18px;height:18px}
.per{left:765px;top:614px;width:73px;height:30px}
.per-label{left:855px;top:622px;font-size:12px;color:var(--ink)}
.pg-prev{left:923px;top:614px;width:31px;height:30px;background:#e2e4e8;display:flex;align-items:center;justify-content:center}
.pg-next{left:1086px;top:614px;width:31px;height:30px;background:var(--brand);border-radius:2px;display:flex;align-items:center;justify-content:center}
.pages{left:964px;top:622px;font-size:11px;color:var(--soft);display:flex;gap:8px}
.pages .cur{color:var(--brand);font-weight:600;text-decoration:underline}
.footer{left:61px;top:713px;width:1139px;height:62px;background:var(--white)}
</style>
</head>
<body>

<nav class="abs sidebar">
  <svg class="side-icon" style="top:19px" viewBox="0 0 24 24" fill="#fff"><path d="M12 2 2 7v2h20V7z"/><rect x="4" y="10" width="3" height="8"/><rect x="10.5" y="10" width="3" height="8"/><rect x="17" y="10" width="3" height="8"/><rect x="2" y="19" width="20" height="3"/></svg>
  <svg class="side-icon" style="top:79px" viewBox="0 0 24 24" fill="#fff"><rect x="3" y="3" width="8" height="11"/><rect x="13" y="3" width="8" height="6"/><rect x="13" y="11" width="8" height="10"/><rect x="3" y="16" width="8" height="5"/></svg>
  <div class="side-active"></div>
  <svg class="side-icon" style="top:135px" viewBox="0 0 24 24" fill="#fff"><rect x="6" y="2" width="11" height="5" transform="rotate(30 11 5)"/><rect x="9" y="8" width="12" height="3" transform="rotate(30 15 9)"/><rect x="2" y="19" width="14" height="3"/></svg>
  <svg class="side-icon" style="top:191px" viewBox="0 0 24 24" fill="#fff"><circle cx="12" cy="7" r="4.5"/><path d="M3 22c0-6 4-9 9-9s9 3 9 9z"/></svg>
  <svg class="side-icon" style="top:248px" viewBox="0 0 24 24" fill="#fff"><path d="M12 2a6 6 0 0 0-6 6v6l-2 3h16l-2-3V8a6 6 0 0 0-6-6z"/><circle cx="12" cy="20" r="2.2"/></svg>
  <svg class="side-icon" style="top:303px" viewBox="0 0 24 24" fill="none" stroke="#fff" stroke-width="2"><path d="M20 11 12 19a5 5 0 0 1-7-7l9-9a3.5 3.5 0 0 1 5 5l-9 9a2 2 0 0 1-3-3l8-8"/></svg>
  <svg class="side-icon" style="top:360px" viewBox="0 0 24 24" fill="none" stroke="#fff" stroke-width="2"><circle cx="12" cy="12" r="9"/><path d="M12 7v5l-3 2"/></svg>
  <svg class="side-icon" style="top:417px" viewBox="0 0 24 24" fill="#fff"><path d="M10 2h4l1 3 3-1 2 3-2 2 1 3 3 1v4l-3 1-1 3 2 2-3 3-2-2-3 1-1 3h-4l-1-3-3-1-2 2-3-3 2-2-1-3-3-1v-4l3-1 1-3-2-2 3-3 2 2 3-1z" transform="scale(.85) translate(2 -1)"/><circle cx="12" cy="11" r="3" fill="#1d4f91"/></svg>
  <svg class="side-icon" style="top:473px" viewBox="0 0 24 24" fill="none" stroke="#fff" stroke-width="2.4"><path d="M10 6 4 12l6 6M4 12h12M16 5h4v14h-4"/></svg>
  <svg class="side-icon" style="top:726px" viewBox="0 0 24 24" stroke="#fff" stroke-width="2"><path d="M4 7h16M4 12h16M4 17h16"/></svg>
</nav>

<header class="abs topbar"></header>
<svg class="abs" style="left:101px;top:21px" width="18" height="18" viewBox="0 0 24 24" fill="none" stroke="#1d4f91" stroke-width="2.6"><circle cx="10" cy="10" r="7"/><path d="M15 15l6 6"/></svg>
<div class="abs search-label">Search</div>
<div class="abs add-btn"><span class="plus"><svg width="10" height="10" viewBox="0 0 10 10" stroke="#fff" stroke-width="2"><path d="M5 0v10M0 5h10"/></svg></span>Add New</div>
<svg class="abs" style="left:923px;top:19px" width="22" height="22" viewBox="0 0 24 24" fill="none" stroke="#1d4f91" stroke-width="2"><path d="M4 12a8 8 0 1 0 2.5-5.8"/><path d="M3 4v4h4"/><path d="M12 8v4l3 2"/></svg>
<svg class="abs" style="left:975px;top:19px" width="22" height="22" viewBox="0 0 24 24" fill="none" stroke="#1d4f91" stroke-width="1.8"><path d="M12 3a6 6 0 0 0-6 6v5l-2 3h16l-2-3V9a6 6 0 0 0-6-6z"/><path d="M10 20a2 2 0 0 0 4 0"/></svg>
<div class="abs avatar" role="img" aria-label="User profile photo"></div>
<div class="abs user-name">Elric Vance</div>
<svg class="abs" style="left:1164px;top:25px" width="11" height="8" viewBox="0 0 11 8" fill="none" stroke="#2e3440" stroke-width="2"><path d="M1 1l4.5 5L10 1"/></svg>

<main>
  <div class="abs card"></div>
  <div class="abs toolbar"></div>
  <div class="abs tab active" style="left:135px;top:117px">My Matters</div>
  <div class="abs tab-underline"></div>
  <div class="abs tab" style="left:234px;top:119px">Recent Matters</div>
  <div class="abs tab" style="left:342px;top:119px">All Matters</div>
  <div class="abs ctl" style="left:431px;top:111px;width:144px;height:30px">Saved Searches
    <svg style="position:absolute;right:12px" width="11" height="7" viewBox="0 0 11 7" fill="none" stroke="#1d4f91" stroke-width="2"><path d="M1 1l4.5 4.5L10 1"/></svg></div>
  <div class="abs ctl" style="left:590px;top:111px;width:160px;height:30px">Filters</div>
  <div class="abs export"><svg width="15" height="14" viewBox="0 0 16 14" fill="#fff"><rect x="4" y="0" width="8" height="4"/><rect x="0" y="4" width="16" height="7" rx="1"/><rect x="4" y="8" width="8" height="6" fill="#fff" stroke="#1d4f91"/></svg>Export</div>

  <div class="abs th" style="left:141px">Title</div>
  <div class="abs th" style="left:592px">Client</div>
  <div class="abs th" style="left:723px">Practice Area</div>
  <div class="abs th" style="left:879px">Status</div>
  <div class="abs th" style="left:1046px">Last Updated</div>

  <div class="abs row-line" style="top:199px"></div>
  <div class="abs row-line" style="top:245px"></div>
  <div class="abs row-line" style="top:292px"></div>
  <div class="abs row-line" style="top:338px"></div>
  <div class="abs row-line" style="top:385px"></div>
  <div class="abs row-line" style="top:431px"></div>
  <div class="abs row-line" style="top:478px"></div>
  <div class="abs row-line" style="top:525px"></div>
  <div class="abs row-line" style="top:572px"></div>

  <div class="abs td" style="left:141px;top:216px">Harlow v. Pennick concerningsale #707</div><div class="abs td" style="left:592px;top:216px">R Castell</div><div class="abs td" style="left:723px;top:216px">Conveyancing</div><div class="abs td" style="left:879px;top:216px">Conveyancing</div><div class="abs td" style="left:1046px;top:216px">30/06/2017</div>
  <div class="abs td" style="left:141px;top:262px">Harlow v. Pennick concerningsale #707</div><div class="abs td" style="left:592px;top:262px">R Castell</div><div class="abs td" style="left:723px;top:262px">Conveyancing</div><div class="abs td" style="left:879px;top:262px">Conveyancing</div><div class="abs td" style="left:1046px;top:262px">30/06/2017</div>
  <div class="abs td" style="left:141px;top:308px">Harlow v. Pennick concerningsale #707</div><div class="abs td" style="left:592px;top:308px">R Castell</div><div class="abs td" style="left:723px;top:308px">Conveyancing</div><div class="abs td" style="left:879px;top:308px">Conveyancing</div><div class="abs td" style="left:1046px;top:308px">30/06/2017</div>
  <div class="abs td" style="left:141px;top:355px">Harlow v. Pennick concerningsale #707</div><div class="abs td" style="left:592px;top:355px">R Castell</div><div class="abs td" style="left:723px;top:355px">Conveyancing</div><div class="abs td" style="left:879px;top:355px">Conveyancing</div><div class="abs td" style="left:1046px;top:355px">30/06/2017</div>
  <div class="abs td" style="left:141px;top:401px">Harlow v. Pennick concerningsale #707</div><div class="abs td" style="left:592px;top:401px">R Castell</div><div class="abs td" style="left:723px;top:401px">Conveyancing</div><div class="abs td" style="left:879px;top:401px">Conveyancing</div><div class="abs td" style="left:1046px;top:401px">30/06/2017</div>
  <div class="abs td" style="left:141px;top:448px">Harlow v. Pennick concerningsale #707</div><div class="abs td" style="left:592px;top:448px">R Castell</div><div class="abs td" style="left:723px;top:448px">Conveyancing</div><div class="abs td" style="left:879px;top:448px">Conveyancing</div><div class="abs td" style="left:1046px;top:448px">30/06/2017</div>
  <div class="abs td" style="left:141px;top:495px">Harlow v. Pennick concerningsale #707</div><div class="abs td" style="left:592px;top:495px">R Castell</div><div class="abs td" style="left:723px;top:495px">Conveyancing</div><div class="abs td" style="left:879px;top:495px">Conveyancing</div><div class="abs td" style="left:1046px;top:495px">30/06/2017</div>
  <div class="abs td" style="left:141px;top:542px">Harlow v. Pennick concerningsale #707</div><div class="abs td" style="left:592px;top:542px">R Castell</div><div class="abs td" style="left:723px;top:542px">Conveyancing</div><div class="abs td" style="left:879px;top:542px">Conveyancing</div><div class="abs td" style="left:1046px;top:542px">30/06/2017</div>

  <div class="abs ctl per" style="font-size:10px">10
    <svg style="position:absolute;right:12px" width="11" height="7" viewBox="0 0 11 7" fill="none" stroke="#1d4f91" stroke-width="2"><path d="M1 1l4.5 4.5L10 1"/></svg></div>
  <div class="abs per-label">Per Page</div>
  <div class="abs pg-prev"><svg width="8" height="12" viewBox="0 0 8 12" fill="none" stroke="#fff" stroke-width="2"><path d="M6 1 1 6l5 5"/></svg></div>
  <div class="abs pages"><span class="cur">1</span><span>2</span><span>3</span><span>4</span><span>5</span><span>6</span><span>7</span><span>8</span></div>
  <div class="abs pg-next"><svg width="8" height="12" viewBox="0 0 8 12" fill="none" stroke="#fff" stroke-width="2"><path d="M2 1l5 5-5 5"/></svg></div>
</main>

<div class="abs menu-caret"></div>
<div class="abs menu">
  <div class="menu-head">Add</div>
  <div class="menu-item"><svg viewBox="0 0 24 24" fill="none" stroke="#1d4f91" stroke-width="2"><circle cx="12" cy="12" r="9"/><path d="M12 7v5l-3 2"/></svg>Time</div>
  <div class="menu-item hover"><svg viewBox="0 0 24 24" fill="none" stroke="#1d4f91" stroke-width="2"><path d="M20 11 12 19a5 5 0 0 1-7-7l9-9a3.5 3.5 0 0 1 5 5l-9 9a2 2 0 0 1-3-3l8-8"/></svg>Document</div>
  <div class="menu-item"><svg viewBox="0 0 24 24" fill="#1d4f91"><path d="M12 2a6 6 0 0 0-6 6v6l-2 3h16l-2-3V8a6 6 0 0 0-6-6z"/><circle cx="12" cy="20" r="2.2"/></svg>Task</div>
  <div class="menu-item"><svg viewBox="0 0 24 24" fill="#1d4f91"><rect x="5" y="2" width="14" height="20" rx="1"/><path d="M8 8h8M8 12h8M8 16h6" stroke="#fff" stroke-width="1.5"/></svg>Notes</div>
  <div class="menu-item"><svg viewBox="0 0 24 24" fill="#1d4f91"><rect x="6" y="2" width="11" height="5" transform="rotate(30 11 5)"/><rect x="9" y="8" width="12" height="3" transform="rotate(30 15 9)"/><rect x="2" y="19" width="14" height="3"/></svg>Matter</div>
  <div class="menu-item"><svg viewBox="0 0 24 24" fill="#1d4f91"><circle cx="12" cy="7" r="4.5"/><path d="M3 22c0-6 4-9 9-9s9 3 9 9z"/></svg>Contact</div>
</div>

<footer class="abs footer"></footer>
</body>
</html>
```